Torvel, Inc. new buisness cards - brand guide included

We need new business cards. SLEAK SIMPLE FINANCE. They must include a place for NAME, TITLE, CELL, OFFICE PHONE, EMAIL. they also must include our services across the bottom. AIR, OCEAN, FTL, LTL, EXPRESS. for reference this will be being handed to some of the most prestigious shipping companies in a america.

Target Market(s)

Finance and corporate

Contact Information for Business Card

We need new business cards. SLEAK SIMPLE FINANCE. They must include a place for NAME, TITLE, CELL, OFFICE PHONE, EMAIL. they also must include our services across the bottom. AIR, OCEAN, FTL, LTL, EXPRESS.

Requirements
Must have
• We need new business cards. SLEAK SIMPLE FINANCE. They must include a place for NAME, TITLE, CELL, OFFICE PHONE, EMAIL. they also must include our services across the bottom. AIR, OCEAN, FTL, LTL, EXPRESS.
Nice to have
• USE THE COLORS AND LOGO IN THE BRAND GUIDE :)

```html
<!DOCTYPE html>
<html lang="en">
<head>
<meta charset="UTF-8">
<title>Torvel, Inc. Business Card</title>
<link href="https://fonts.googleapis.com/css2?family=Montserrat:wght@400;500;600&display=swap" rel="stylesheet">
<style>
  :root {
    --canvas: #e4e8e8;
    --ink: #2e2e2e;
    --paper: #ffffff;
    --rule: #2e2e2e;
  }
  html, body {
    margin: 0;
    padding: 0;
    width: 1200px;
    height: 900px;
    overflow: hidden;
    background: var(--canvas);
    font-family: "Montserrat", Arial, sans-serif;
  }
  .sheet {
    width: 1200px;
    height: 900px;
    display: flex;
    align-items: center;
    justify-content: center;
    gap: 40px;
  }
  .card {
    width: 540px;
    height: 309px;
    position: relative;
    box-sizing: border-box;
    box-shadow: 0 2px 6px rgba(0,0,0,0.12);
  }
  .card--front {
    background: var(--ink);
    display: flex;
    align-items: center;
    justify-content: center;
  }
  .brand-name {
    font-weight: 500;
    letter-spacing: 0.08em;
    margin: 0;
  }
  .card--front .brand-name {
    color: var(--paper);
    font-size: 34px;
  }
  .card--back {
    background: var(--paper);
    color: var(--ink);
  }
  .back-brand {
    position: absolute;
    left: 34px;
    top: 150px;
    display: flex;
    align-items: center;
    gap: 8px;
  }
  .back-brand .mark {
    width: 14px;
    height: 14px;
    background: var(--ink);
  }
  .back-brand .brand-name {
    font-size: 17px;
    color: var(--ink);
  }
  .details {
    position: absolute;
    left: 232px;
    top: 78px;
    width: 270px;
  }
  .person-name {
    font-size: 23px;
    font-weight: 600;
    letter-spacing: 0.02em;
    margin: 0;
    line-height: 1.05;
  }
  .person-title {
    font-size: 17px;
    font-weight: 500;
    margin: 2px 0 14px;
    line-height: 1.1;
  }
  .contact-list {
    list-style: none;
    margin: 0;
    padding: 0;
  }
  .contact-list li {
    display: flex;
    align-items: center;
    gap: 12px;
    font-size: 14px;
    height: 24px;
  }
  .contact-list svg {
    width: 14px;
    height: 14px;
    flex: none;
  }
  .services {
    margin-top: 16px;
    border-top: 1.5px solid var(--rule);
    padding-top: 8px;
    font-size: 12.5px;
    font-weight: 500;
    letter-spacing: 0.04em;
    white-space: nowrap;
  }
</style>
</head>
<body>
<main class="sheet">
  <section class="card card--front">
    <p class="brand-name">Torvel, Inc.</p>
  </section>

  <section class="card card--back">
    <div class="back-brand">
      <span class="mark"></span>
      <p class="brand-name">Torvel, Inc.</p>
    </div>

    <div class="details">
      <h1 class="person-name">YOUR NAME</h1>
      <p class="person-title">YOUR TITLE</p>
      <ul class="contact-list">
        <li>
          <svg viewBox="0 0 14 14" aria-hidden="true">
            <circle cx="7" cy="7" r="7" fill="#2e2e2e"/>
            <path d="M4.6 3.8 L5.8 3.6 L6.3 5.2 L5.5 5.8 Q6.2 7.6 8 8.5 L8.6 7.7 L10.2 8.2 L10 9.4 Q6.8 9.8 4.6 6.6 Q4.2 5 4.6 3.8Z" fill="#fff"/>
          </svg>
          +1 (000) 000-0000
        </li>
        <li>
          <svg viewBox="0 0 14 14" aria-hidden="true">
            <circle cx="7" cy="7" r="7" fill="#2e2e2e"/>
            <rect x="4.3" y="5.2" width="5.4" height="4.6" rx="0.6" fill="#fff"/>
            <rect x="5.2" y="3.6" width="3.6" height="1.4" fill="#fff"/>
            <rect x="5.3" y="6.2" width="3.4" height="0.8" fill="#2e2e2e"/>
          </svg>
          +1 (000) 000-0000
        </li>
        <li>
          <svg viewBox="0 0 14 14" aria-hidden="true">
            <circle cx="7" cy="7" r="7" fill="#2e2e2e"/>
            <rect x="3.8" y="4.6" width="6.4" height="4.8" fill="none" stroke="#fff" stroke-width="0.9"/>
            <path d="M3.9 4.7 L7 7.2 L10.1 4.7" fill="none" stroke="#fff" stroke-width="0.9"/>
          </svg>
          your email here
        </li>
      </ul>
      <p class="services">AIR | OCEAN | FTL | LTL | EXPRESS</p>
    </div>
  </section>
</main>
</body>
</html>
```